Garnett and Lyle Personal Injury Billboard

We'd like a clean/modern billboard to build brand awareness for our law firm in the area of personal injury. Ideally, we like the word "Injured?" or something similar in large lettering.

I'm attaching images, logo and award badges which could be used. The billboards will be 14x48 ft and 10.6x36.

We are open to different color ideas, fonts, and artwork. Creative but not too busy with wording. Our web page is www.kgarnettfirm.example

Garnett & Lyle Law Firm
(555) 318-4092

```html
<!DOCTYPE html>
<html lang="en">
<head>
<meta charset="UTF-8">
<title>Garnett &amp; Lyle Law Firm — Injured? Billboard</title>
<link rel="stylesheet" href="https://fonts.googleapis.com/css2?family=Open+Sans:wght@700&family=Montserrat:wght@300;400;600&display=swap">
<style>
  :root {
    --page-bg: #ffffff;
    --board-black: #050304;
    --photo-light: #8a8a8a;
    --photo-mid: #4a4a4a;
    --text-white: #ffffff;
    --accent-blue: #29abe2;
    --badge-blue: #2a9fd6;
    --badge-edge: #1c6f98;
  }
  * { margin: 0; padding: 0; box-sizing: border-box; }
  html, body {
    width: 1025px;
    height: 1200px;
    overflow: hidden;
    background: var(--page-bg);
  }
  .billboard {
    position: absolute;
    left: 32px;
    top: 458px;
    width: 961px;
    height: 283px;
    background: var(--board-black);
    overflow: hidden;
    box-shadow: 0 8px 10px -4px rgba(0,0,0,0.25);
  }
  .billboard__photo {
    position: absolute;
    left: 0;
    top: 0;
    width: 300px;
    height: 100%;
    background: linear-gradient(90deg, var(--photo-light) 0%, var(--photo-mid) 55%, var(--board-black) 100%);
  }
  .firm-name {
    position: absolute;
    left: 37px;
    top: 120px;
    color: var(--text-white);
    font-family: "Montserrat", sans-serif;
    font-weight: 600;
    line-height: 1.08;
  }
  .firm-name__main {
    display: block;
    font-size: 27px;
  }
  .firm-name__sub {
    display: block;
    font-size: 13px;
    letter-spacing: 3px;
    margin-top: 6px;
  }
  .headline {
    position: absolute;
    left: 330px;
    width: 570px;
    top: 12px;
    text-align: center;
    color: var(--text-white);
    font-family: "Open Sans", sans-serif;
    font-weight: 700;
    font-size: 104px;
    letter-spacing: -1px;
    line-height: 1.2;
  }
  .tagline {
    position: absolute;
    left: 392px;
    top: 141px;
    width: 385px;
    height: 39px;
    background: var(--accent-blue);
  }
  .tagline__text {
    position: absolute;
    left: 0;
    width: 100%;
    top: -16px;
    text-align: center;
    color: var(--text-white);
    font-family: "Montserrat", sans-serif;
    font-weight: 400;
    font-size: 53px;
    line-height: 1.1;
    white-space: nowrap;
  }
  .contact {
    position: absolute;
    left: 330px;
    width: 570px;
    text-align: center;
    color: var(--text-white);
    font-family: "Montserrat", sans-serif;
    white-space: nowrap;
  }
  .contact--phone {
    top: 194px;
    font-size: 26px;
    font-weight: 400;
  }
  .contact--web {
    top: 232px;
    font-size: 21px;
    font-weight: 300;
    letter-spacing: 0.5px;
  }
  .award-badge {
    position: absolute;
    left: 875px;
    top: 197px;
    width: 47px;
    height: 65px;
    background: var(--badge-blue);
    border: 2px solid var(--badge-edge);
  }
</style>
</head>
<body>
  <section class="billboard">
    <div class="billboard__photo" role="img" aria-label="Black-and-white photo of a man in a tank top holding his bandaged wrist in pain"></div>

    <div class="firm-name">
      <span class="firm-name__main">Garnett &amp; Lyle</span>
      <span class="firm-name__sub">Law Firm</span>
    </div>

    <h1 class="headline">Injured?</h1>

    <div class="tagline">
      <p class="tagline__text">We can help!</p>
    </div>

    <p class="contact contact--phone">Call US: (555) 318-4092</p>
    <p class="contact contact--web">www.kgarnettfirm.example</p>

    <div class="award-badge" role="img" aria-label="Community award winner badge"></div>
  </section>
</body>
</html>
```